CEO of company needs clear business card that stands out from the rest

I need a clear business card (standard credit card size) for the CEO/Founder of our company...Brightfield Counseling. We would like to see designs that use our logo colors, which are khaki, chocolate brown, and gray. The card should be an edgy design, maybe where half the card is transparent with curves on the card, or a textured card where the logo is transparent, I don't care much for white cards. The final design should communicate a funky, edgy, and modern look, as well as stand out to have the "WOW" factor. The information we need on the card would be Name, Title, Toll free number, Phone Number, address, email address, and website.

*PLEASE SEND FRONT AND BACK OF CARDS

Card is two sided front and back please give us your front and back designs

The card should be an edgy design, maybe where half the card is transparent with curves on the card, or a textured card where the logo is transparent, I don't care much for white cards. The final design should communicate a funky, edgy, and modern look, as well as stand out to have the "WOW" factor.

Please follow these guidelines for the card

SPECS (card):

2.125 (h) x 3.375 (w) card size after cut

2.375 (h) x 3.625 (w) card with bleed

300 dpi

cmyk

1/8 bleed

allow 1/8 border for live area

I will also attached the pdf for the information listed above which includes a diagram of the card

 

All the cards need to have rounded edges

I just updated a card as an example of how you can use different fonts on a single business card, look how the name is written in script, so what I am saying is make this a card you will be proud to design and put it in your portfolio 

Reason: this race is really close and I am working with 2 designers to fine tune their designs and the weekend is slowing us down

• Our Logo
MUST HAVE PARTS OF CARD THAT ARE TRANSPARENT. See ideas that are attached.
Card is two sided front and back
• The final design should communicate a funky, edgy, and modern look, as well as stand out to have the "WOW" factor. The information we need on the card would be Name, Title, Toll free number, Phone Number, address, email address, and website.

```html
<!DOCTYPE html>
<html lang="en">
<head>
<meta charset="utf-8">
<title>Brightfield Counseling – Business Card</title>
<link href="https://fonts.googleapis.com/css2?family=Questrial&family=Roboto:wght@300;400&display=swap" rel="stylesheet">
<style>
  :root{
    --bg:#2a1a12;
    --gold-light:#e0a437;
    --gold:#c98a1c;
    --gold-deep:#9a6410;
    --brown:#7a5a3a;
    --paper:#ffffff;
    --ink:#b98a4a;
    --rule:#e3cfae;
  }
  *{box-sizing:border-box;margin:0;padding:0}
  html,body{width:1200px;height:720px;overflow:hidden;background:var(--bg)}
  .stage{position:relative;width:1200px;height:720px;display:flex;align-items:center;justify-content:center;gap:60px}
  .card{position:relative;width:520px;height:328px;border-radius:18px;overflow:hidden;
    background:linear-gradient(135deg,var(--gold-light) 0%,var(--gold) 45%,var(--gold-deep) 100%);
    box-shadow:0 14px 30px rgba(0,0,0,.45)}
  /* front */
  .front .brand{position:absolute;left:0;right:0;top:120px;display:flex;align-items:center;justify-content:center;gap:14px}
  .brand-dot{width:34px;height:34px;border-radius:50%;background:var(--brown)}
  .brand-name{font-family:"Questrial",sans-serif;font-size:34px;color:var(--brown);letter-spacing:.5px;white-space:nowrap}
  .front .tagline{position:absolute;left:0;right:0;top:176px;text-align:center;font-family:"Questrial",sans-serif;font-size:15px;color:var(--brown);letter-spacing:1.5px}
  /* back */
  .logo-panel{position:absolute;right:0;top:0;width:258px;height:132px;background:var(--paper);border-bottom-left-radius:16px;
    display:flex;flex-direction:column;align-items:center;justify-content:center;gap:8px}
  .logo-panel .brand{display:flex;align-items:center;gap:8px}
  .logo-panel .brand-dot{width:18px;height:18px;background:var(--ink)}
  .logo-panel .brand-name{font-size:20px;color:var(--ink)}
  .logo-panel .tagline{font-family:"Questrial",sans-serif;font-size:10px;color:var(--ink);letter-spacing:1px;white-space:nowrap}
  .info-panel{position:absolute;left:0;bottom:0;width:350px;height:170px;background:var(--paper);border-top-right-radius:16px;
    display:flex;font-family:"Roboto",sans-serif;color:var(--ink)}
  .identity{width:132px;border-right:1px solid var(--rule);padding:18px 12px;display:flex;flex-direction:column;justify-content:flex-end}
  .identity .name{font-size:19px;font-weight:300;letter-spacing:1px;line-height:1.1;white-space:nowrap}
  .identity .title{font-size:10px;letter-spacing:1.5px;margin-top:4px;white-space:nowrap}
  .contact{flex:1;padding:18px 12px;list-style:none;display:flex;flex-direction:column;justify-content:center;gap:9px}
  .contact li{display:flex;align-items:center;gap:9px;font-size:10px;font-weight:300;letter-spacing:.5px;white-space:nowrap}
  .contact svg{width:14px;height:14px;flex:none;fill:none;stroke:var(--ink);stroke-width:1.6}
</style>
</head>
<body>
<main class="stage">
  <section class="card front" aria-label="Card front">
    <div class="brand"><span class="brand-dot"></span><span class="brand-name">Brightfield Counseling</span></div>
    <p class="tagline">a steady path toward recovery</p>
  </section>

  <section class="card back" aria-label="Card back">
    <div class="logo-panel">
      <div class="brand"><span class="brand-dot"></span><span class="brand-name">Brightfield Counseling</span></div>
      <p class="tagline">a steady path toward recovery</p>
    </div>
    <div class="info-panel">
      <div class="identity">
        <p class="name">YOUR NAME</p>
        <p class="title">TITLE HERE</p>
      </div>
      <ul class="contact">
        <li><svg viewBox="0 0 16 16"><path d="M3 2l3 1 1 3-2 1a8 8 0 004 4l1-2 3 1 1 3-2 1C7 14 2 9 2 4z"/></svg>0800 555 010 247</li>
        <li><svg viewBox="0 0 16 16"><rect x="4" y="1.5" width="8" height="13" rx="1.5"/><path d="M7 12h2"/></svg>0201 555 0199</li>
        <li><svg viewBox="0 0 16 16"><circle cx="8" cy="8" r="6"/><path d="M2 8h12M8 2c3 3 3 9 0 12M8 2c-3 3-3 9 0 12"/></svg>WWW.BRIGHTFIELDCARE.ORG</li>
        <li><svg viewBox="0 0 16 16"><rect x="1.5" y="3.5" width="13" height="9" rx="1"/><path d="M2 4l6 5 6-5"/></svg>HELLO@BRIGHTFIELDCARE.ORG</li>
        <li><svg viewBox="0 0 16 16"><path d="M8 15s-5-5-5-8.5a5 5 0 0110 0C13 10 8 15 8 15z"/><circle cx="8" cy="6.5" r="1.8"/></svg>YOUR ADDRESS WILL BE HERE</li>
      </ul>
    </div>
  </section>
</main>
</body>
</html>
```